Business card for apparel company. Specializing in fishing and boating performance wear. Main company name is Marlowe Teal Company, LLC brand name for apparel is WAKEFIN. See website www.WakefinReefline.com I will attach some logos to consider.

```html
<!DOCTYPE html>
<html lang="en">
<head>
<meta charset="utf-8">
<title>WAKEFIN Business Card</title>
<link rel="stylesheet" href="https://fonts.googleapis.com/css2?family=Arimo:wght@400;700&display=swap">
<style>
  :root {
    --bg: #e9ebee;
    --brand-blue: #1f8fd8;
    --deep-blue: #2f5fb4;
    --sky-blue: #22aee6;
    --ink: #2b2f36;
    --muted: #4a4f57;
    --card-white: #ffffff;
    --divider: #3a9ad9;
  }
  * { box-sizing: border-box; margin: 0; padding: 0; }
  html, body {
    width: 1200px; height: 900px; overflow: hidden;
    background: var(--bg);
    font-family: "Arimo", Arial, sans-serif;
  }
  .canvas { position: relative; width: 1200px; height: 900px; }
  .card {
    position: absolute; width: 600px; height: 345px;
    border-radius: 22px; overflow: hidden;
    box-shadow: 0 10px 30px rgba(0,0,0,.18);
  }
  .card--back { left: 110px; top: 80px; }
  .card--front { left: 490px; top: 475px; background: var(--card-white); }

  .back-pattern {
    position: absolute; inset: 0;
    background: linear-gradient(160deg, var(--sky-blue) 0%, #2a86d2 45%, var(--deep-blue) 100%);
  }
  .back-brand {
    position: absolute; inset: 0;
    display: flex; align-items: center; justify-content: center;
    gap: 14px;
  }
  .brand-dot { width: 22px; height: 22px; border-radius: 50%; background: #fff; }
  .back-brand .brand-name {
    color: #fff; font-weight: 700; font-size: 62px; letter-spacing: 4px;
  }

  .front-brand {
    position: absolute; left: 0; right: 0; top: 52px;
    display: flex; align-items: center; justify-content: center; gap: 12px;
  }
  .front-brand .brand-dot { background: var(--brand-blue); width: 18px; height: 18px; }
  .front-brand .brand-name {
    color: var(--brand-blue); font-weight: 700; font-size: 52px; letter-spacing: 3px;
  }

  .person {
    position: absolute; right: 318px; top: 178px; text-align: right;
  }
  .person__name {
    color: var(--brand-blue); font-weight: 700; font-size: 26px; letter-spacing: 1px;
  }
  .person__title { color: var(--muted); font-size: 17px; margin-top: 3px; }

  .divider {
    position: absolute; left: 298px; top: 172px; width: 1.5px; height: 78px;
    background: var(--divider);
  }

  .contacts {
    position: absolute; left: 318px; top: 170px; list-style: none;
  }
  .contacts li {
    display: flex; align-items: center; gap: 10px;
    color: var(--ink); font-size: 16px; line-height: 28px;
  }
  .contacts svg { width: 14px; height: 14px; fill: var(--brand-blue); flex: none; }

  .address {
    position: absolute; left: 0; right: 0; bottom: 40px;
    text-align: center; color: var(--ink); font-size: 18px; letter-spacing: .3px;
  }
</style>
</head>
<body>
<main class="canvas">

  <section class="card card--back">
    <div class="back-pattern" role="img" aria-label="Blue gradient with a faint repeating brand mark pattern"></div>
    <div class="back-brand">
      <span class="brand-dot"></span>
      <span class="brand-name">WAKEFIN</span>
    </div>
  </section>

  <section class="card card--front">
    <div class="front-brand">
      <span class="brand-dot"></span>
      <span class="brand-name">WAKEFIN</span>
    </div>

    <div class="person">
      <p class="person__name">CALLUM REEVE</p>
      <p class="person__title">CEO/Founder</p>
    </div>

    <span class="divider"></span>

    <ul class="contacts">
      <li>
        <svg viewBox="0 0 24 24" aria-hidden="true"><path d="M6.6 10.8a15.1 15.1 0 0 0 6.6 6.6l2.2-2.2a1 1 0 0 1 1-.25 11.4 11.4 0 0 0 3.6.57 1 1 0 0 1 1 1V20a1 1 0 0 1-1 1A17 17 0 0 1 3 4a1 1 0 0 1 1-1h3.5a1 1 0 0 1 1 1c0 1.25.2 2.45.57 3.57a1 1 0 0 1-.25 1z"/></svg>
        (123) 555-0187
      </li>
      <li>
        <svg viewBox="0 0 24 24" aria-hidden="true"><path d="M2 5h20v14H2z M2 5l10 8 10-8" fill="none" stroke="#1f8fd8" stroke-width="2.4"/></svg>
        info@WakefinReefline.com
      </li>
      <li>
        <svg viewBox="0 0 24 24" aria-hidden="true"><circle cx="12" cy="12" r="9.5" fill="none" stroke="#1f8fd8" stroke-width="2"/><path d="M2.5 12h19M12 2.5c3 3 3 16 0 19M12 2.5c-3 3-3 16 0 19" fill="none" stroke="#1f8fd8" stroke-width="1.6"/></svg>
        www.WakefinReefline.com
      </li>
    </ul>

    <p class="address">Po Box 4120 Harbor Lane Bayport AB 3307</p>
  </section>

</main>
</body>
</html>
```